Ridgeback Petroleum Ventures, LLC

Our website (www.ridgebackpetroventures.example) is poorly done and dated. I want to redo it with one main page and wide format photos or oil & gas drilling and production. Perhaps all of the pages listed on the left side of the existing site could be viewed by scrolling down further on the new main page. I want something clean and easy to navigate.

Target Market(s)

Other oil and gas companies and people that we have contacted regarding selling or leasing their mineral rights. These people will come to our website to research our company and become more comfortable doing business with us.

Industry/Entity Type

Oil And Gas

Coding

Coded - Design and coding required

Number of Pages Required

1 page

Font styles to use
Serif

Requirements
Must have
• Clean and uncluttered. Nice, clear wide format picture or oil well or rig and landscape.

```html
<!DOCTYPE html>
<html lang="en">
<head>
<meta charset="utf-8">
<title>Ridgeback Petroleum Ventures</title>
<link href="https://fonts.googleapis.com/css2?family=Montserrat:wght@700&family=Lato:wght@400&family=Tinos:wght@700&display=swap" rel="stylesheet">
<style>
  :root {
    --orange: #e06500;
    --teal: #1abc9c;
    --navy: #2e3e50;
    --white: #ffffff;
    --stone: #ececec;
  }
  * { margin: 0; padding: 0; box-sizing: border-box; }
  html, body { width: 1200px; height: 675px; overflow: hidden; }
  body { position: relative; background: var(--teal); color: var(--white); font-family: "Lato", sans-serif; }

  .site-header {
    position: absolute; top: 0; left: 0; width: 1200px; height: 62px;
    background: var(--orange);
  }
  .brand {
    position: absolute; left: 93px; top: 19px;
    font-family: "Montserrat", sans-serif; font-weight: 700; font-size: 18px;
    letter-spacing: 0.3px; line-height: 24px; color: var(--white);
  }
  .main-nav {
    position: absolute; right: 94px; top: 9px; height: 44px;
    display: flex; list-style: none;
  }
  .main-nav li {
    display: flex; align-items: center; padding: 0 13px;
    font-family: "Tinos", serif; font-weight: 700; font-size: 13px;
    letter-spacing: 0.9px; text-transform: uppercase;
  }
  .main-nav li.is-active { background: var(--teal); }

  .history {
    position: absolute; top: 62px; left: 0; width: 1200px; height: 470px;
    background: var(--teal);
  }
  .section-title {
    position: absolute; top: 69px; left: 0; width: 1200px; text-align: center;
    font-family: "Montserrat", sans-serif; font-weight: 700; font-size: 38px;
    line-height: 46px; letter-spacing: 0.5px;
  }
  .portrait {
    position: absolute; left: 107px; top: 153px; width: 228px; height: 228px;
  }
  .history-text {
    position: absolute; left: 445px; top: 183px; width: 690px;
    font-size: 16.6px; line-height: 25px;
  }

  .divider-band {
    position: absolute; top: 532px; left: 0; width: 1200px; height: 37px;
    background: linear-gradient(180deg, #f1f1f1, var(--stone));
  }
  .next-section {
    position: absolute; top: 569px; left: 0; width: 1200px; height: 106px;
    background: var(--teal);
  }
</style>
</head>
<body>
  <header class="site-header">
    <div class="brand">RIDGEBACK</div>
    <ul class="main-nav">
      <li class="is-active">History</li>
      <li>About</li>
      <li>Find Us</li>
      <li>Contact</li>
    </ul>
  </header>

  <section class="history">
    <h1 class="section-title">HISTORY</h1>
    <svg class="portrait" viewBox="0 0 228 228" role="img" aria-label="Illustration of an oil field worker in a yellow hard hat and tie">
      <circle cx="114" cy="114" r="114" fill="#2e3e50"/>
    </svg>
    <p class="history-text">Ridgeback Petroleum Ventures, LLC was founded in 2011 by Martin Callow. In 2012 Owen Callow &amp; Grant Callow joined the company. Ridgeback has expanded their business, and currently has offices located in Fort Worth and Oklahoma City. Since 2012 Ridgeback has acquired more than 25,000 net acres of leasehold in Texas, Oklahoma and Kansas. During the same time, the company has also purchased several thousand mineral acres in areas of active drilling. In addition, Ridgeback has participated in dozens of wells with top tier operators.</p>
  </section>

  <div class="divider-band"></div>
  <section class="next-section"></section>
</body>
</html>
```